Bright Ridge Painting and Remodeling New Facebook Design Project

Facebook should include company logo.

Name of company: Bright Ridge Painting and Remodeling
Address: 4612 NW 28th st Suite 519
Miami, FL 33174

local phone: (305) 555-0147
toll free (855) 555-0192
fax (866) 555-0136

email: corla@paintingbrightridge.example

let me know if links to other social media should be included.

company does interior and exterior painting, staining, pressure washing, wall paper removal, tile installation, tile removal, specializing in vinyl floor removal and any of your remodeling needs.

we give free estimates.

Designer can add nice pictures of homes showing painting of interior exterior etc.

Or even videos or whatever they feel is necessary to make an impression to consumers.

Be creative. Page should be professional but eye catching.

Reason: I started getting good designs submitted on the last day want to give designers an opportunity to submit more

Industry/Entity Type

Painting And Decorating

Requirements
Must have
• Professional wording/ font and pictures.
• Creative professional design and colors.
Nice to have
• Pictures of the services offered
• Videos about/and or of the services being offered
Should not have
• N/A

```html
<!DOCTYPE html>
<html lang="en">
<head>
<meta charset="utf-8">
<title>Bright Ridge Painting and Remodeling – Cover</title>
<link rel="stylesheet" href="https://fonts.googleapis.com/css2?family=Roboto+Slab:wght@400;700&family=Open+Sans:wght@600;700&family=Share+Tech+Mono&display=swap">
<style>
  :root {
    --white: #ffffff;
    --pink: #f0248a;
    --pink-soft: rgba(236, 64, 150, 0.55);
    --bar: rgba(20, 18, 22, 0.72);
    --ink-shadow: rgba(0, 0, 0, 0.55);
  }
  * { margin: 0; padding: 0; box-sizing: border-box; }
  html, body { width: 1200px; height: 444px; overflow: hidden; background: #222; }
  .cover {
    position: relative;
    width: 1200px;
    height: 444px;
    overflow: hidden;
    font-family: "Open Sans", Arial, sans-serif;
    color: var(--white);
  }
  .scenes { position: absolute; inset: 0; }

  .brand-mark {
    position: absolute;
    left: 30px; top: 26px;
    display: flex; align-items: center; gap: 10px;
  }
  .brand-mark .dot {
    width: 30px; height: 30px; border-radius: 50%;
    background: var(--pink);
  }
  .brand-mark .name {
    font-family: "Roboto Slab", Georgia, serif;
    font-weight: 700;
    font-size: 17px;
    letter-spacing: 0.5px;
    color: var(--white);
  }

  .headline {
    position: absolute;
    left: 30px; top: 136px;
    text-shadow: 2px 2px 6px var(--ink-shadow);
  }
  .headline h1 {
    font-family: "Roboto Slab", Georgia, serif;
    font-weight: 700;
    font-size: 54px;
    line-height: 1;
    letter-spacing: 1px;
  }
  .headline .tagline {
    font-family: "Roboto Slab", Georgia, serif;
    font-weight: 400;
    font-size: 21px;
    letter-spacing: 4px;
    line-height: 1.35;
    margin-top: 8px;
    text-transform: uppercase;
  }

  .contact-button {
    position: absolute;
    left: 30px; top: 336px;
    width: 182px; height: 34px;
    background: var(--pink);
    clip-path: polygon(6% 0, 100% 0, 94% 100%, 0 100%);
    display: flex; align-items: center; justify-content: center;
    font-weight: 700; font-size: 17px; letter-spacing: 0.5px;
  }

  .call-block {
    position: absolute;
    right: 30px; top: 286px;
    text-align: right;
    text-shadow: 1px 1px 4px var(--ink-shadow);
  }
  .call-block h2 {
    font-weight: 700; font-size: 25px; letter-spacing: 1px;
    margin-right: 30px;
  }
  .call-block p {
    font-family: "Share Tech Mono", "Courier New", monospace;
    font-size: 17px; line-height: 1.2;
  }

  .info-bar {
    position: absolute;
    left: 0; bottom: 0;
    width: 1200px; height: 66px;
    background: var(--bar);
    display: flex; align-items: center;
    font-weight: 700; font-size: 19px;
  }
  .info-item { position: absolute; display: flex; align-items: center; gap: 14px; }
  .info-item svg { flex: none; }
  .info-email { left: 30px; }
  .info-address { left: 520px; line-height: 1.05; font-size: 20px; }
  .info-phone { left: 950px; font-weight: 600; font-size: 21px; }
</style>
</head>
<body>
<div class="cover">
  <svg class="scenes" width="1200" height="444" viewBox="0 0 1200 444" xmlns="http://www.w3.org/2000/svg">
    <defs>
      <linearGradient id="bedroom" x1="0" y1="0" x2="0" y2="1">
        <stop offset="0" stop-color="#3a2a24"/>
        <stop offset="0.5" stop-color="#5a4236"/>
        <stop offset="0.75" stop-color="#4f6b2a"/>
        <stop offset="1" stop-color="#1f1a16"/>
      </linearGradient>
      <linearGradient id="living" x1="0" y1="0" x2="0" y2="1">
        <stop offset="0" stop-color="#8a8c8e"/>
        <stop offset="0.55" stop-color="#b7b4ae"/>
        <stop offset="1" stop-color="#3b2a20"/>
      </linearGradient>
      <linearGradient id="lounge" x1="0" y1="0" x2="1" y2="1">
        <stop offset="0" stop-color="#6d5a3e"/>
        <stop offset="0.45" stop-color="#c9a46b"/>
        <stop offset="0.75" stop-color="#6e8ea2"/>
        <stop offset="1" stop-color="#4c5a48"/>
      </linearGradient>
      <linearGradient id="kitchen" x1="0" y1="0" x2="0" y2="1">
        <stop offset="0" stop-color="#4a4040"/>
        <stop offset="0.5" stop-color="#8a6a64"/>
        <stop offset="1" stop-color="#3a2024"/>
      </linearGradient>
      <linearGradient id="boardroom" x1="0" y1="0" x2="1" y2="1">
        <stop offset="0" stop-color="#c8629a"/>
        <stop offset="0.5" stop-color="#b84a86"/>
        <stop offset="1" stop-color="#7a2458"/>
      </linearGradient>
    </defs>
    <rect role="img" aria-label="Photo of a bedroom with a green bedspread and dark wood floor" x="0" y="0" width="242" height="444" fill="url(#bedroom)"/>
    <rect role="img" aria-label="Photo of a bright living room with a red armchair" x="242" y="0" width="246" height="444" fill="url(#living)"/>
    <rect role="img" aria-label="Photo of a warm lounge opening onto a glass patio" x="488" y="0" width="240" height="444" fill="url(#lounge)"/>
    <rect role="img" aria-label="Photo of a modern kitchen with pink pendant lights" x="728" y="0" width="472" height="444" fill="url(#kitchen)"/>
    <polygon role="img" aria-label="Photo of a pink-lit conference room" points="985,0 1200,0 1200,444 760,444" fill="url(#boardroom)" opacity="0.92"/>
    <polygon points="985,0 1200,0 1200,444 760,444" fill="var(--pink-soft)"/>
    <line x1="242" y1="0" x2="238" y2="444" stroke="#fff" stroke-opacity="0.5" stroke-width="2"/>
    <line x1="488" y1="0" x2="486" y2="444" stroke="#fff" stroke-opacity="0.5" stroke-width="2"/>
    <line x1="728" y1="0" x2="726" y2="444" stroke="#fff" stroke-opacity="0.5" stroke-width="2"/>
    <line x1="985" y1="0" x2="760" y2="444" stroke="#ff7ab8" stroke-width="3"/>
  </svg>

  <div class="brand-mark">
    <span class="dot"></span>
    <span class="name">BRIGHT RIDGE</span>
  </div>

  <div class="headline">
    <h1>BRIGHT RIDGE</h1>
    <p class="tagline">Painting and<br>Remodeling</p>
  </div>

  <div class="contact-button">CONTACT US</div>

  <div class="call-block">
    <h2>CALL US</h2>
    <p>Toll free &nbsp;(855) 555-0192</p>
    <p>Fax &nbsp;(866) 555-0136</p>
  </div>

  <div class="info-bar">
    <div class="info-item info-email">
      <svg width="34" height="26" viewBox="0 0 34 26" aria-hidden="true">
        <rect x="2" y="2" width="30" height="22" fill="none" stroke="#fff" stroke-width="2.5"/>
        <polyline points="2,2 17,15 32,2" fill="none" stroke="#fff" stroke-width="2.5"/>
      </svg>
      <span>corla@paintingbrightridge.example</span>
    </div>
    <div class="info-item info-address">
      <svg width="36" height="32" viewBox="0 0 36 32" aria-hidden="true">
        <polyline points="2,16 18,3 34,16" fill="none" stroke="#fff" stroke-width="2.5"/>
        <polyline points="7,12 7,30 29,30 29,12" fill="none" stroke="#fff" stroke-width="2.5"/>
        <rect x="14" y="18" width="8" height="12" fill="none" stroke="#fff" stroke-width="2"/>
      </svg>
      <span>4612 NW 28th st Suite 519<br>Miami, FL 33174</span>
    </div>
    <div class="info-item info-phone">
      <svg width="28" height="30" viewBox="0 0 28 30" aria-hidden="true">
        <path d="M6 2 L11 2 L13 9 L9 12 C11 17 14 20 18 22 L21 18 L27 21 L27 26 C27 28 25 29 23 29 C12 27 3 18 2 7 C2 4 4 2 6 2 Z" fill="#fff"/>
      </svg>
      <span>305 555-0147</span>
    </div>
  </div>
</div>
</body>
</html>
```